Design some Business Cards

Create a set of business cards for council of Marrowden.
The cards should be somehow indicative of the level/ status age group of the members, which i why a small description of the stages is included.
The card should look professional and colours and designs should match or complement the initial scheme.

```html
<!DOCTYPE html>
<html lang="en">
<head>
<meta charset="utf-8">
<title>Council of Marrowden – Business Cards</title>
<link href="https://fonts.googleapis.com/css2?family=Open+Sans:wght@400;600;700&display=swap" rel="stylesheet">
<style>
  :root {
    --page: #e4e6e5;
    --card-white: #f5f5f5;
    --forest: #3e5a52;
    --leaf: #7ba33d;
    --mark: #587a6c;
    --ink: #222a27;
    --ink-soft: #4b5652;
    --on-forest: #ffffff;
  }
  * { box-sizing: border-box; margin: 0; padding: 0; }
  html, body {
    width: 1200px; height: 900px; overflow: hidden;
    background: var(--page);
    font-family: "Open Sans", Arial, sans-serif;
  }
  .sheet {
    position: relative; width: 1200px; height: 900px;
  }
  .card {
    position: absolute; left: 250px; width: 700px; height: 400px;
    background: var(--card-white); overflow: hidden;
    box-shadow: 0 6px 18px rgba(0,0,0,0.15);
  }
  .card--back { top: 40px; }
  .card--front { top: 470px; }

  /* shared brand mark */
  .brand { display: flex; align-items: center; gap: 12px; }
  .brand__dot { width: 26px; height: 26px; border-radius: 50%; background: var(--leaf); }
  .brand__name { font-weight: 600; color: var(--mark); letter-spacing: 2px; }

  /* back card */
  .card--back .brand { position: absolute; left: 0; right: 0; top: 92px; justify-content: center; }
  .card--back .brand__name { font-size: 64px; }
  .back__tagline {
    position: absolute; top: 186px; left: 0; right: 0; text-align: center;
    font-size: 19px; color: var(--mark); font-weight: 600;
  }
  .back__band {
    position: absolute; left: 0; right: 0; bottom: 0; height: 140px;
    background: var(--forest);
  }
  .back__web {
    position: absolute; left: 0; right: 0; top: 22px; text-align: center;
    font-size: 15px; color: var(--on-forest);
  }

  /* front card */
  .front__shape { position: absolute; inset: 0; }
  .front__identity { position: absolute; left: 40px; top: 36px; }
  .front__identity .brand__name { font-size: 44px; }
  .person { margin-top: 14px; }
  .person__name { font-size: 22px; font-weight: 700; color: var(--ink); }
  .person__role { font-size: 14px; color: var(--ink-soft); margin-top: 2px; }
  .contacts { position: absolute; left: 40px; top: 214px; list-style: none; }
  .contacts li {
    display: flex; align-items: center; gap: 12px;
    font-size: 14px; color: var(--ink); height: 36px;
  }
  .contacts svg { width: 18px; height: 18px; flex: none; }
  .front__org {
    position: absolute; right: 40px; top: 52px;
    font-size: 22px; color: var(--on-forest); font-weight: 400;
  }
  .front__address {
    position: absolute; right: 40px; bottom: 46px; text-align: right;
    font-size: 15px; line-height: 1.5; color: var(--on-forest);
  }
</style>
</head>
<body>
<main class="sheet">

  <section class="card card--back" aria-label="Card back">
    <div class="brand">
      <span class="brand__name">COM</span>
      <span class="brand__dot"></span>
    </div>
    <p class="back__tagline">Council of Marrowden</p>
    <div class="back__band">
      <p class="back__web">www.marrowdencouncil.org</p>
    </div>
  </section>

  <section class="card card--front" aria-label="Card front">
    <svg class="front__shape" viewBox="0 0 700 400" preserveAspectRatio="none" aria-hidden="true">
      <polygon points="420,0 700,0 700,400 290,400" fill="var(--forest)"/>
    </svg>

    <div class="front__identity">
      <div class="brand">
        <span class="brand__name">COM</span>
        <span class="brand__dot"></span>
      </div>
      <div class="person">
        <p class="person__name">Your Name Here</p>
        <p class="person__role">President &amp; CEO</p>
      </div>
    </div>

    <ul class="contacts">
      <li>
        <svg viewBox="0 0 24 24"><circle cx="12" cy="12" r="10.5" fill="none" stroke="var(--ink)" stroke-width="2"/><path d="M8.5 7.5l2 2-1 1.5c.8 1.6 1.9 2.7 3.5 3.5l1.5-1 2 2-1.5 1.5c-3.5-.5-7.5-4.5-8-8z" fill="var(--ink)"/></svg>
        +44 1632 960 418
      </li>
      <li>
        <svg viewBox="0 0 24 24"><rect x="7" y="2" width="10" height="20" rx="2" fill="var(--ink)"/><rect x="9" y="5" width="6" height="12" fill="var(--card-white)"/></svg>
        +44 1632 960 418
      </li>
      <li>
        <svg viewBox="0 0 24 24"><rect x="2" y="5" width="20" height="14" rx="1.5" fill="var(--ink)"/><path d="M3 6l9 7 9-7" fill="none" stroke="var(--card-white)" stroke-width="1.6"/></svg>
        hello@marrowdencouncil.org
      </li>
      <li>
        <svg viewBox="0 0 24 24"><circle cx="12" cy="12" r="10" fill="none" stroke="var(--ink)" stroke-width="2"/><ellipse cx="12" cy="12" rx="4.5" ry="10" fill="none" stroke="var(--ink)" stroke-width="1.6"/><path d="M2 12h20" stroke="var(--ink)" stroke-width="1.6"/></svg>
        www.marrowdencouncil.org
      </li>
    </ul>

    <p class="front__org">Council of Marrowden</p>
    <p class="front__address">14 Harrow Lane, Suite 3<br>Marrowden, MR4 7QT, England</p>
  </section>

</main>
</body>
</html>
```